Pitch deck power point presentation template

I need a power point template for a pitch deck for a startup biotechnology company using the logo we purchased from pixelharbor. It should have a cover page and content pages that we can adapt to fit multiple presentations. It should have a page for the team and advisors, and pages for graphs and charts, also pages that have space to add pictures to give background information, and then some with general pages with some blank space. I want it to catch the eye but also be very professional looking.
Updates

The original deadline was only one day from posting for some reason, I extended to 5 days to allow more time.

Target Market(s)

Investors

Industry/Entity Type

Biotechnology

Font styles to use
Serif
Sans Serif

Colors
0054AA
0677BA
7BADD7
CADEEF
E8F1F8

Requirements
Must have
• The logo and the blue color from the logo as the primary color used
Nice to have
• other layouts that we can select from

```html
<!DOCTYPE html>
<html lang="en">
<head>
<meta charset="utf-8">
<title>Corvane Therapeutics – Pitch Deck Template</title>
<link href="https://fonts.googleapis.com/css2?family=Poppins:wght@300;400;500;600;700;800&family=Roboto:wght@400;500;700&display=swap" rel="stylesheet">
<style>
:root{
  --teal:#14a08e;
  --blue:#1a95d5;
  --blue-deep:#0677ba;
  --navy:#1c2c46;
  --ink:#3a3a3a;
  --muted:#6b6b6b;
  --panel:#e7e8e9;
  --line:#d5d8db;
  --sky:#cadeef;
  --mist:#e8f1f8;
  --desk:#a4a8ab;
}
*{box-sizing:border-box;margin:0;padding:0}
html,body{width:906px;height:1200px;overflow:hidden;background:var(--desk)}
.canvas{position:relative;width:906px;height:1200px;background:var(--desk);font-family:"Roboto",sans-serif;color:var(--ink)}
.slide{position:absolute;width:271px;height:152px;background:#fff;overflow:hidden;box-shadow:1px 2px 4px rgba(0,0,0,.35)}
.abs{position:absolute}
.chart-lines{fill:none}
.footer-bar{position:absolute;left:0;bottom:4px;width:228px;height:5px;background:var(--blue)}
.page-num{position:absolute;right:6px;bottom:3px;width:13px;height:13px;border:1px solid var(--teal);border-radius:50%;background:#fff;font:600 4px "Poppins",sans-serif;color:var(--navy);display:flex;align-items:center;justify-content:center}
.brand{position:absolute;top:7px;right:8px;display:flex;align-items:center;gap:2px;color:var(--blue)}
.brand i{width:7px;height:7px;border:1.2px solid var(--teal);border-radius:50%;display:block}
.brand span{display:flex;flex-direction:column;line-height:.9;font-family:"Poppins",sans-serif;font-weight:600}
.brand b{font-weight:600;font-size:8px}
.brand small{font-size:3px;font-weight:600}
.h-thin{font-family:"Poppins",sans-serif;font-weight:400;color:var(--teal);line-height:1.05}
.h-bold{font-family:"Poppins",sans-serif;font-weight:800;color:var(--teal);line-height:1.05}
.h-blue{color:var(--blue)}
.txt{font-size:2.7px;line-height:1.3;color:var(--muted);text-align:justify}
.label{font-family:"Poppins",sans-serif;font-weight:600;font-size:4px;color:var(--teal)}
.photo{position:absolute}
.ticks{list-style:none;font-size:4px;color:var(--ink)}
.ticks li{margin-bottom:6.5px;padding-left:7px;position:relative}
.ticks li::before{content:"✓";position:absolute;left:0;color:var(--navy);font-size:4px}
.squares{list-style:none;font-size:5px;color:var(--ink)}
.squares li{margin-bottom:4.6px;padding-left:9px;position:relative}
.squares li::before{content:"";position:absolute;left:0;top:1.5px;width:3px;height:3px;background:var(--teal)}
.arrow-item{position:absolute;font-size:2.6px;line-height:1.3;color:var(--muted);padding-left:9px}
.arrow-item::before{content:"";position:absolute;left:0;top:1px;border-left:3px solid var(--blue);border-top:2px solid transparent;border-bottom:2px solid transparent}
.arrow-item.hollow::before{border-left-color:var(--sky)}
.legend{position:absolute;width:52px}
.legend b{display:block;font-size:3.6px;color:var(--blue);font-weight:500;position:relative;padding-left:5px}
.legend b::before{content:"";position:absolute;left:0;top:.8px;width:2.6px;height:2.6px;border-radius:50%;background:var(--blue)}
.legend p{font-size:2.3px;line-height:1.3;color:var(--muted);padding-left:5px}
.contents-item{position:absolute;left:148px;width:112px;border-left:.7px solid var(--teal);padding-left:5px}
.contents-item b{font-size:4.2px;color:var(--teal);font-weight:500}
.contents-item p{font-size:2.6px;line-height:1.3;color:var(--muted)}
.ring{position:absolute;border-radius:50%;display:flex;flex-direction:column;align-items:center;justify-content:center}
.edu-box{position:absolute;width:46px;height:67px;border:1.4px solid var(--blue);border-radius:4px;background:#fff;text-align:center;padding:6px 3px 0}
.edu-box b{display:block;font:500 4.2px "Poppins",sans-serif;color:var(--navy);margin:2px 0}
.edu-box p{font-size:2.3px;line-height:1.3;color:var(--ink)}
.mini-col{position:absolute;font-size:2.4px;line-height:1.3;color:var(--muted);text-align:center}
.mini-col b{display:block;font-size:3.6px;color:var(--blue);font-weight:500;margin-bottom:1px}
.person{position:absolute;top:70px;width:52px;text-align:center;color:#fff}
.person .avatar{width:22px;height:22px;margin:0 auto 2px;border-radius:50%;border:1.5px solid #fff;background:linear-gradient(#d9e6ef,#9bb8cc)}
.person b{display:block;font:600 4px "Poppins",sans-serif;color:var(--navy)}
.person p{font-size:2.3px;line-height:1.3;color:#fff}
</style>
</head>
<body>
<div class="canvas">

<!-- 01 Cover -->
<section class="slide" style="left:39px;top:36px">
  <div class="photo" role="img" aria-label="Light blue DNA double helix artwork" style="left:110px;top:0;width:161px;height:152px;background:linear-gradient(120deg,#ffffff 0%,#e3f0fa 35%,#a9d0ef 70%,#e8f3fb 100%)"></div>
  <div class="abs" style="left:14px;top:15px;display:flex;align-items:center;gap:3px;color:var(--blue);font-family:'Poppins',sans-serif;font-weight:600">
    <i style="display:block;width:12px;height:12px;border:2px solid var(--blue);border-radius:50%"></i>
    <span style="display:flex;flex-direction:column;line-height:.85"><b style="font-size:17px;font-weight:600">Corvane</b><small style="font-size:6px;font-weight:600;margin-left:9px">Therapeutics</small></span>
  </div>
  <div class="h-thin abs" style="left:14px;top:78px;font-size:6.5px">PRESENTATION</div>
  <div class="h-bold h-blue abs" style="left:14px;top:86px;font-size:16px">BUSINESS</div>
  <div class="h-bold abs" style="left:14px;top:104px;font-size:15.5px">MARKETING</div>
  <div class="abs" style="left:14px;top:129px;width:75px;height:.8px;background:var(--teal)"></div>
  <div class="abs" style="left:14px;top:137px;font-size:4px;letter-spacing:1.6px;color:var(--muted)">www.corvane.com</div>
</section>

<!-- 02 Contents -->
<section class="slide" style="left:320px;top:36px">
  <div class="photo" role="img" aria-label="Scientist's hand holding a glowing DNA model" style="left:0;top:0;width:135px;height:145px;background:linear-gradient(160deg,#dfe9f1 0%,#8fb2cb 45%,#30506d 100%)"></div>
  <div class="abs" style="left:0;top:143px;width:135px;height:6px;background:var(--blue)"></div>
  <div class="abs" style="left:93px;top:71px;background:#fff;border-radius:7px 0 0 7px;padding:1px 4px;font:600 12px 'Poppins',sans-serif;color:var(--blue);width:52px;white-space:nowrap">Contents</div>
  <div class="brand"><i></i><span><b>Corvane</b><small>Therapeutics</small></span></div>
  <div class="contents-item" style="top:30px"><b>Lorem ipsum</b><p>A short note on this part of the plan and its key points here.</p></div>
  <div class="contents-item" style="top:55px"><b>Lorem ipsum</b><p>A short note on this part of the plan and its key points here.</p></div>
  <div class="contents-item" style="top:86px"><b>Lorem ipsum</b><p>A short note on this part of the plan and its key points here.</p></div>
  <div class="contents-item" style="top:111px"><b>Lorem ipsum</b><p>A short note on this part of the plan and its key points here.</p></div>
  <div class="page-num">02</div>
</section>

<!-- 03 Domain with photo -->
<section class="slide" style="left:600px;top:36px">
  <div class="abs" style="left:20px;top:18px;width:12px;height:12px;border-left:2px solid var(--blue);border-top:2px solid var(--blue)"></div>
  <div class="abs" style="left:125px;top:118px;width:12px;height:12px;border-right:2px solid var(--teal);border-bottom:2px solid var(--teal)"></div>
  <div class="photo" role="img" aria-label="Researcher using a laboratory microscope" style="left:25px;top:24px;width:108px;height:102px;background:linear-gradient(135deg,#e9f2f9,#9ec3df 55%,#5d88aa)"></div>
  <div class="brand"><i></i><span><b>Corvane</b><small>Therapeutics</small></span></div>
  <div class="h-thin abs" style="left:145px;top:22px;font-size:7.5px;line-height:1.45">WHAT'S A DOMAIN?<br>IT'S THAT NAME UP<br><b style="font-weight:600;font-size:8.8px">IN THE ADDRESS BAR.</b></div>
  <ul class="ticks abs" style="left:145px;top:64px">
    <li>Fits your business or products</li><li>Is easy to spell and remember</li><li>Fits your business or products</li><li>Is easy to spell and remember</li><li>Fits your business or products</li><li>Is easy to spell and remember</li>
  </ul>
  <div class="footer-bar"></div><div class="page-num">03</div>
</section>

<!-- 04 Two columns -->
<section class="slide" style="left:39px;top:200px">
  <div class="abs" style="left:13px;top:13px;width:122px;height:126px;background:var(--panel)"></div>
  <div class="brand"><i></i><span><b>Corvane</b><small>Therapeutics</small></span></div>
  <div class="abs" style="left:22px;top:19px;width:108px">
    <div class="h-thin" style="font-size:8.5px">LOREM IPSUM</div>
    <div class="h-bold" style="font-size:8.5px;font-weight:700">DOLOR SIT AMET</div>
    <p class="txt" style="margin-top:4px">Our team builds new tools for cell research. We test each idea with care and share clear data with partners and investors at every stage of work, from early trials to the clinic.</p>
    <p class="txt" style="margin-top:3px">Our team builds new tools for cell research. We test each idea with care and share clear data with partners and investors at every stage of work, from early trials to the clinic.</p>
  </div>
  <div class="arrow-item" style="left:22px;top:104px;width:108px">Brief point on results for this part of the plan and key aims.</div>
  <div class="arrow-item hollow" style="left:22px;top:120px;width:108px">Brief point on results for this part of the plan and key aims.</div>
  <div class="abs" style="left:146px;top:19px;width:112px">
    <div class="h-thin" style="font-size:8.5px">LOREM IPSUM</div>
    <div class="h-bold" style="font-size:8.5px;font-weight:700">DOLOR SIT AMET</div>
    <p class="txt" style="margin-top:4px">Our team builds new tools for cell research. We test each idea with care and share clear data with partners and investors at every stage of work, from early trials to the clinic.</p>
    <p class="txt" style="margin-top:3px">Our team builds new tools for cell research. We test each idea with care and share clear data with partners and investors at every stage of work, from early trials to the clinic.</p>
  </div>
  <div class="arrow-item" style="left:146px;top:104px;width:108px">Brief point on results for this part of the plan and key aims.</div>
  <div class="arrow-item hollow" style="left:146px;top:120px;width:108px">Brief point on results for this part of the plan and key aims.</div>
  <div class="footer-bar"></div><div class="page-num">04</div>
</section>

<!-- 05 Market opportunities -->
<section class="slide" style="left:320px;top:200px">
  <div class="brand"><i></i><span><b>Corvane</b><small>Therapeutics</small></span></div>
  <div class="abs" style="left:14px;top:14px">
    <div class="h-thin" style="font-size:11px;font-weight:300">MARKET</div>
    <div class="h-bold" style="font-size:11px;font-weight:700">OPPORTUNITIES</div>
  </div>
  <p class="txt abs" style="left:14px;top:45px;width:125px">Our team builds new tools for cell research. We test each idea with care and share clear data with partners and investors at every stage of work.</p>
  <p class="txt abs" style="left:14px;top:62px;width:125px">Our team builds new tools for cell research. We test each idea with care and share clear data with partners.</p>
  <div class="abs" style="left:160px;top:20px;font:700 2.6px 'Poppins',sans-serif">LOREM IPSUM</div>
  <div class="abs" style="left:207px;top:20px;font:700 2.6px 'Poppins',sans-serif">LOREM IPSUM</div>
  <div class="ring" style="left:155px;top:27px;width:38px;height:38px;border:2px solid var(--teal);border-bottom-color:#e2e2e2"><b style="font:700 6.5px 'Poppins',sans-serif;letter-spacing:.8px">4356</b><small style="font-size:1.8px">LOREM IPSUM</small></div>
  <div class="ring" style="left:202px;top:27px;width:38px;height:38px;border:2px solid var(--teal);border-bottom-color:#e2e2e2;border-left-color:#e2e2e2"><b style="font:700 6.5px 'Poppins',sans-serif;letter-spacing:.8px">2164</b><small style="font-size:1.8px">LOREM IPSUM</small></div>
  <svg class="abs" style="left:8px;top:80px" width="135" height="58" viewBox="0 0 135 58">
    <g font-size="2.4" fill="#888" font-family="Roboto"><text x="0" y="3">1000</text><text x="0" y="13">700</text><text x="0" y="23">500</text><text x="0" y="33">300</text><text x="0" y="43">100</text><text x="0" y="53">0</text></g>
    <path d="M12 55 C20 55 24 40 32 44 C38 47 40 53 46 53 C52 53 56 36 66 38 C74 40 74 46 80 45 C88 44 88 20 98 20 C108 20 106 50 122 48 L122 55 Z" fill="var(--blue)"/>
    <g font-size="3.4" font-weight="700" fill="var(--navy)" font-family="Poppins"><text x="27" y="40">100</text><text x="42" y="49">20</text><text x="61" y="33">275</text><text x="75" y="41">130</text><text x="92" y="16">650</text><text x="118" y="44">80</text></g>
  </svg>
  <svg class="abs" style="left:148px;top:80px" width="115" height="58" viewBox="0 0 115 58">
    <g class="chart-lines" stroke="#e0e0e0" stroke-width=".4">
      <path d="M6 4H112M6 12H112M6 20H112M6 28H112M6 36H112M6 44H112M6 52H112"/>
      <path d="M6 4V52M20 4V52M34 4V52M48 4V52M62 4V52M76 4V52M90 4V52M104 4V52"/>
    </g>
    <g fill="none" stroke="var(--teal)" stroke-width=".7">
      <path d="M6 50 C20 20 30 14 48 16 S80 10 104 8"/>
      <path d="M6 50 C20 28 30 24 48 22 S80 26 104 14"/>
      <path d="M6 50 C18 34 32 30 48 30 S80 24 104 20"/>
      <path d="M6 50 C18 40 34 36 48 36 S80 32 104 28"/>
    </g>
    <rect x="40" y="6" width="18" height="5" fill="var(--teal)"/><text x="42" y="9.6" font-size="2.4" fill="#fff" font-family="Roboto">TEXT HERE</text>
  </svg>
  <div class="footer-bar"></div><div class="page-num">05</div>
</section>

<!-- 06 Company overview -->
<section class="slide" style="left:600px;top:200px">
  <div class="brand"><i></i><span><b>Corvane</b><small>Therapeutics</small></span></div>
  <div class="abs" style="left:16px;top:16px">
    <div class="h-thin" style="font-size:9px;font-weight:600">COMPANY</div>
    <div class="h-bold" style="font-size:12.5px;font-weight:700">OVERVIEW</div>
  </div>
  <p class="txt abs" style="left:16px;top:46px;width:108px">Our team builds new tools for cell research. We test each idea with care and share clear data with partners and investors at every stage of work.</p>
  <p class="txt abs" style="left:16px;top:67px;width:108px">Our team builds new tools for cell research and shares clear data.</p>
  <svg class="abs" style="left:130px;top:24px" width="132" height="62" viewBox="0 0 132 62">
    <g font-size="2.8" fill="#666" font-family="Roboto"><text x="0" y="3">60</text><text x="0" y="11.5">50</text><text x="0" y="20">40</text><text x="0" y="28.5">30</text><text x="0" y="37">20</text><text x="0" y="45.5">10</text><text x="1" y="54">0</text></g>
    <g class="chart-lines" stroke="#d9d9d9" stroke-width=".4"><path d="M8 2H130M8 10.5H130M8 19H130M8 27.5H130M8 36H130M8 44.5H130"/><path d="M8 2V53H130V2"/></g>
    <rect x="16" y="19" width="3.5" height="34" fill="var(--blue)"/><rect x="21" y="10" width="3.5" height="43" fill="var(--teal)"/>
    <rect x="42" y="43" width="3.5" height="10" fill="var(--blue)"/><rect x="47" y="23" width="3.5" height="30" fill="var(--teal)"/>
    <rect x="72" y="6" width="3.5" height="47" fill="var(--blue)"/><rect x="77" y="41" width="3.5" height="12" fill="var(--teal)"/>
    <rect x="98" y="12" width="3.5" height="41" fill="var(--teal)"/><rect x="103" y="28" width="3.5" height="25" fill="var(--blue)"/>
    <g font-size="3.2" fill="#444" font-family="Roboto"><text x="15" y="59">JAN</text><text x="41" y="59">FEB</text><text x="71" y="59">MAR</text><text x="97" y="59">APR</text></g>
  </svg>
  <svg class="abs" style="left:10px;top:88px" width="118" height="50" viewBox="0 0 118 50">
    <g font-size="2.4" fill="#666"><text x="0" y="3">60</text><text x="0" y="10">50</text><text x="0" y="17">40</text><text x="0" y="24">30</text><text x="0" y="31">20</text><text x="0" y="38">10</text><text x="1" y="45">0</text></g>
    <g class="chart-lines" stroke="#ddd" stroke-width=".4"><path d="M6 2H116M6 9H116M6 16H116M6 23H116M6 30H116M6 37H116M6 44H116"/></g>
    <polyline fill="none" stroke="var(--teal)" stroke-width=".6" points="10,36 20,42 30,34 40,22 50,30 60,20 70,34 80,28 90,32 100,26 110,40"/>
    <polyline fill="none" stroke="var(--blue)" stroke-width=".6" points="10,40 20,36 30,28 40,32 50,26 60,30 70,26 80,34 90,28 100,22 110,24"/>
    <g font-size="1.8" fill="#777"><text x="8" y="49">TEXT 01</text><text x="28" y="49">TEXT 03</text><text x="48" y="49">TEXT 05</text><text x="68" y="49">TEXT 07</text><text x="88" y="49">TEXT 09</text></g>
  </svg>
  <div class="legend" style="left:137px;top:97px"><b>Lorem ipsum</b><p>Short note on the key point of this part here.</p></div>
  <div class="legend" style="left:202px;top:97px"><b>Lorem ipsum</b><p>Short note on the key point of this part here.</p></div>
  <div class="legend" style="left:137px;top:116px"><b>Lorem ipsum</b><p>Short note on the key point of this part here.</p></div>
  <div class="legend" style="left:202px;top:116px"><b>Lorem ipsum</b><p>Short note on the key point of this part here.</p></div>
  <div class="footer-bar"></div><div class="page-num">06</div>
</section>

<!-- 07 Active intelligence -->
<section class="slide" style="left:39px;top:364px">
  <div class="brand"><i></i><span><b>Corvane</b><small>Therapeutics</small></span></div>
  <div class="abs" style="left:13px;top:15px">
    <div class="h-thin" style="font-size:8.5px;font-weight:500">ACTIVE</div>
    <div class="h-bold" style="font-size:8.5px;font-weight:700">INTELLIGENCE</div>
  </div>
  <p class="txt abs" style="left:13px;top:39px;width:110px">Our team builds new tools for cell research. We test each idea with care and share clear data with partners and investors at every stage of work, from early trials through to the clinic and beyond.</p>
  <p class="txt abs" style="left:13px;top:67px;width:110px">Our team builds new tools for cell research. We test each idea with care and share clear data with partners and investors at every stage of work, from early trials through to the clinic and beyond.</p>
  <div class="arrow-item" style="left:13px;top:105px;width:108px">Brief point on results for this part of the plan and key aims ahead.</div>
  <div class="arrow-item hollow" style="left:13px;top:122px;width:108px">Brief point on results for this part of the plan and key aims ahead.</div>
  <div class="abs" style="left:191px;top:25px;width:60px;height:1.6px;background:var(--blue)"></div>
  <div class="abs" style="left:129px;top:100px;width:2px;height:36px;background:var(--teal)"></div>
  <div class="abs" style="left:129px;top:134px;width:40px;height:2px;background:var(--teal)"></div>
  <div class="photo" role="img" aria-label="Lab researcher in protective gear with a digital interface overlay" style="left:133px;top:29px;width:138px;height:103px;background:linear-gradient(135deg,#c9e0ef,#5f94bb 55%,#23506f)"></div>
  <div class="footer-bar"></div><div class="page-num">07</div>
</section>

<!-- 08 Market opportunities chart -->
<section class="slide" style="left:320px;top:364px">
  <div class="brand"><i></i><span><b>Corvane</b><small>Therapeutics</small></span></div>
  <div class="abs" style="left:14px;top:14px">
    <div class="h-bold" style="font-size:11px;font-weight:700">MARKET</div>
    <div class="h-bold" style="font-size:11px;font-weight:700">OPPORTUNITIES</div>
  </div>
  <p class="txt abs" style="left:14px;top:43px;width:104px">Our team builds new tools for cell research. We test each idea with care and share clear data with partners and investors at every stage of work.</p>
  <p class="txt abs" style="left:14px;top:64px;width:104px">Our team builds new tools for cell research and shares clear data.</p>
  <div class="abs" style="left:137px;top:15px;font:600 3.4px 'Poppins',sans-serif">CONSECTETUER ADIPISCING</div>
  <svg class="abs" style="left:130px;top:21px" width="100" height="60" viewBox="0 0 100 60">
    <g font-size="2.8" fill="#444"><text x="0" y="3">60</text><text x="0" y="11">50</text><text x="0" y="19">40</text><text x="0" y="27">30</text><text x="0" y="35">20</text><text x="0" y="43">10</text><text x="1" y="51">0</text></g>
    <g class="chart-lines" stroke="#ddd" stroke-width=".4"><path d="M7 2H98M7 10H98M7 18H98M7 26H98M7 34H98M7 42H98"/><path d="M7 2V50H98V2"/></g>
    <rect x="13" y="18" width="11" height="32" fill="var(--blue)"/><rect x="35" y="4" width="11" height="46" fill="var(--teal)"/>
    <rect x="57" y="38" width="11" height="12" fill="var(--blue)"/><rect x="79" y="14" width="11" height="36" fill="var(--teal)"/>
    <g font-size="3.2" fill="#333"><text x="14" y="56">JAN</text><text x="36" y="56">FEB</text><text x="57" y="56">MAR</text><text x="80" y="56">APR</text></g>
  </svg>
  <svg class="abs" style="left:12px;top:86px" width="76" height="50" viewBox="0 0 76 50">
    <ellipse cx="38" cy="27" rx="36" ry="19" fill="#0e7f71"/>
    <path d="M38 6 A36 19 0 0 1 74 24 L60 24 A22 10 0 0 0 38 15 Z" fill="var(--blue)"/>
    <path d="M74 24 A36 19 0 0 1 38 43 L38 34 A22 10 0 0 0 60 24 Z" fill="var(--teal)"/>
    <path d="M38 43 A36 19 0 0 1 2 24 A36 19 0 0 1 38 6 L38 15 A22 10 0 0 0 16 24 A22 10 0 0 0 38 34 Z" fill="var(--teal)"/>
    <path d="M38 34 A22 10 0 0 1 22 30 L38 43 Z" fill="var(--blue)"/>
    <g font-size="4.5" font-weight="700" fill="#fff" font-family="Poppins"><text x="46" y="11">20%</text><text x="60" y="30">20%</text><text x="4" y="27">40%</text><text x="40" y="41">20%</text></g>
  </svg>
  <div class="legend" style="left:98px;top:95px;width:60px"><b>Lorem ipsum</b><p>Short note on the key point of this part of the plan.</p></div>
  <div class="legend" style="left:173px;top:95px;width:60px"><b>Lorem ipsum</b><p>Short note on the key point of this part of the plan.</p></div>
  <div class="legend" style="left:98px;top:117px;width:60px"><b>Lorem ipsum</b><p>Short note on the key point of this part of the plan.</p></div>
  <div class="legend" style="left:173px;top:117px;width:60px"><b>Lorem ipsum</b><p>Short note on the key point of this part of the plan.</p></div>
  <div class="footer-bar"></div><div class="page-num">08</div>
</section>

<!-- 09 Pin infographic -->
<section class="slide" style="left:600px;top:364px">
  <div class="brand"><i></i><span><b>Corvane</b><small>Therapeutics</small></span></div>
  <div class="abs h-bold" style="left:13px;top:9px;font-size:8px;font-weight:700">LOREM IPSUM <span style="font-weight:800">DOLOR SIT AMET</span></div>
  <svg class="abs" style="left:0;top:24px" width="271" height="118" viewBox="0 0 271 118">
    <polyline fill="none" stroke="var(--teal)" stroke-width=".5" stroke-dasharray="1 1" points="49,13 88,19 128,6 168,2 208,7"/>
    <g fill="#fff" stroke="var(--teal)" stroke-width=".8"><circle cx="49" cy="13" r="2"/><circle cx="88" cy="19" r="2"/><circle cx="128" cy="6" r="2"/><circle cx="168" cy="2" r="2"/><circle cx="208" cy="7" r="2"/></g>
    <g font-size="3" font-weight="700" fill="var(--navy)" font-family="Poppins"><text x="43" y="9">$1000</text><text x="83" y="15">$750</text><text x="122" y="3">$1200</text><text x="162" y="-1">$1400</text><text x="203" y="3">$1100</text></g>
    <g>
      <path d="M49 16 L35 49 L49 60 Z" fill="var(--blue)"/><path d="M49 16 L63 49 L49 60 Z" fill="#0f76b0"/>
      <path d="M88 22 L74 49 L88 60 Z" fill="var(--teal)"/><path d="M88 22 L102 49 L88 60 Z" fill="#0c7e70"/>
      <path d="M128 9 L114 49 L128 60 Z" fill="var(--blue)"/><path d="M128 9 L142 49 L128 60 Z" fill="#0f76b0"/>
      <path d="M168 5 L154 49 L168 60 Z" fill="var(--teal)"/><path d="M168 5 L182 49 L168 60 Z" fill="#0c7e70"/>
      <path d="M208 10 L194 49 L208 60 Z" fill="var(--blue)"/><path d="M208 10 L222 49 L208 60 Z" fill="#0f76b0"/>
    </g>
    <g fill="#fff"><circle cx="40" cy="50" r="3"/><circle cx="79" cy="50" r="3"/><circle cx="119" cy="50" r="3"/><circle cx="159" cy="50" r="3"/><circle cx="199" cy="50" r="3"/></g>
    <g font-size="3.2" fill="#fff" font-family="Poppins" font-weight="600">
      <text transform="translate(52 44) rotate(-90)">Title One</text><text transform="translate(91 44) rotate(-90)">Title Two</text><text transform="translate(131 44) rotate(-90)">Title Three</text><text transform="translate(171 44) rotate(-90)">Title Four</text>
    </g>
    <g font-size="2.6" font-weight="700" fill="var(--navy)"><text x="45" y="67">2014</text><text x="84" y="67">2016</text><text x="124" y="67">2018</text><text x="164" y="67">2020</text><text x="204" y="67">2023</text></g>
    <g fill="none" stroke="var(--blue)" stroke-width="1"><path d="M43 71 L49 75 L55 71M82 71 L88 75 L94 71M122 71 L128 75 L134 71M162 71 L168 75 L174 71M202 71 L208 75 L214 71"/></g>
  </svg>
  <div class="mini-col" style="left:29px;top:104px;width:38px;text-align:left">Short note on the year and its key result for this stage.</div>
  <div class="mini-col" style="left:69px;top:104px;width:38px;text-align:left">Short note on the year and its key result for this stage.</div>
  <div class="mini-col" style="left:109px;top:104px;width:38px;text-align:left">Short note on the year and its key result for this stage.</div>
  <div class="mini-col" style="left:149px;top:104px;width:38px;text-align:left">Short note on the year and its key result for this stage.</div>
  <div class="mini-col" style="left:189px;top:104px;width:38px;text-align:left">Short note on the year and its key result for this stage.</div>
  <div class="footer-bar"></div><div class="page-num">09</div>
</section>

<!-- 10 Company stats -->
<section class="slide" style="left:39px;top:528px">
  <div class="brand"><i></i><span><b>Corvane</b><small>Therapeutics</small></span></div>
  <div class="abs h-bold" style="left:14px;top:16px;font-size:8.5px;font-weight:700;color:var(--blue)">COMPANY <span style="color:var(--teal)">IPSUM SIT</span></div>
  <p class="txt abs" style="left:14px;top:28px;width:245px">Our team builds new tools for cell research. We test each idea with care and share clear data with partners and investors at every stage of work, from early trials through to the clinic and beyond, with a clear plan.</p>
  <p class="txt abs" style="left:14px;top:44px;width:245px">Our team builds new tools for cell research. We test each idea with care and share clear data with partners and investors at every stage of work.</p>
  <div class="ring" style="left:13px;top:71px;width:36px;height:36px;border:2.4px solid var(--teal);border-left-color:#e2e2e2"><b style="font:400 9px 'Poppins',sans-serif;color:var(--teal)">75%</b><small style="font-size:2.8px;color:var(--teal)">LOREM IPSUM</small></div>
  <div class="ring" style="left:76px;top:71px;width:36px;height:36px;border:2.4px solid var(--teal);border-left-color:#e2e2e2;border-bottom-color:#e2e2e2"><b style="font:400 9px 'Poppins',sans-serif;color:var(--teal)">50%</b><small style="font-size:2.4px;color:var(--teal);text-align:center;line-height:1">PRETIUM<br>VOLUTPAT</small></div>
  <div class="mini-col" style="left:13px;top:112px;width:40px">Short note on this key figure for the year.</div>
  <div class="mini-col" style="left:75px;top:112px;width:40px">Short note on this key figure for the year.</div>
  <svg class="abs" style="left:150px;top:66px" width="110" height="66" viewBox="0 0 110 66">
    <g font-size="2.8" fill="#333"><text x="0" y="3">80</text><text x="0" y="10.5">70</text><text x="0" y="18">60</text><text x="0" y="25.5">50</text><text x="0" y="33">40</text><text x="0" y="40.5">30</text><text x="0" y="48">20</text><text x="0" y="55.5">10</text></g>
    <g class="chart-lines" stroke="var(--blue)" stroke-width=".4" stroke-dasharray="1 1"><path d="M10 2V58M20 2V58M30 2V58M40 2V58M50 2V58M60 2V58M70 2V58M80 2V58M90 2V58"/></g>
    <g fill="var(--teal)"><rect x="9" y="29" width="2" height="29"/><rect x="19" y="49" width="2" height="9"/><rect x="29" y="40" width="2" height="18"/><rect x="39" y="14" width="2" height="44"/><rect x="49" y="8" width="2" height="50"/><rect x="59" y="28" width="2" height="30"/><rect x="69" y="36" width="2" height="22"/><rect x="79" y="32" width="2" height="26"/><rect x="89" y="6" width="2" height="52"/></g>
    <g font-size="2.8" fill="var(--blue)"><text x="7" y="63">JAN</text><text x="17" y="63">FEB</text><text x="26" y="63">MAR</text><text x="37" y="63">APR</text><text x="47" y="63">MAY</text><text x="57" y="63">JUN</text><text x="68" y="63">JUL</text><text x="77" y="63">AUG</text><text x="88" y="63">SEP</text></g>
  </svg>
  <div class="footer-bar"></div><div class="page-num">10</div>
</section>

<!-- 11 Education -->
<section class="slide" style="left:320px;top:528px">
  <div class="brand"><i></i><span><b>Corvane</b><small>Therapeutics</small></span></div>
  <div class="abs h-bold" style="left:9px;top:10px;font-size:10px;font-weight:600;color:var(--blue)"><span style="font-weight:400">OUR COMPANY</span> EDUCATION</div>
  <div class="photo" role="img" aria-label="Faint world map in the background" style="left:30px;top:30px;width:215px;height:85px;background:radial-gradient(ellipse at center,#eef1f4 0%,#ffffff 75%)"></div>
  <svg class="abs" style="left:0;top:0" width="271" height="152" viewBox="0 0 271 152">
    <path d="M95 46 C105 46 100 70 110 70M160 46 C170 46 165 70 175 70" fill="none" stroke="var(--blue)" stroke-width="1.4"/>
    <g fill="var(--teal)"><circle cx="95" cy="46" r="2.2"/><circle cx="110" cy="70" r="2.2"/><circle cx="160" cy="46" r="2.2"/><circle cx="175" cy="70" r="2.2"/></g>
  </svg>
  <div class="edu-box" style="left:46px;top:36px"><svg width="8" height="8" viewBox="0 0 8 8"><circle cx="4" cy="3" r="2.3" fill="none" stroke="#333" stroke-width=".6"/><path d="M3 6H5M3.2 7H4.8" stroke="#333" stroke-width=".6"/></svg><b>IDEA</b><p>Short note on this first stage and the plan for the team and partners in the year.</p></div>
  <div class="edu-box" style="left:111px;top:36px"><svg width="8" height="8" viewBox="0 0 8 8"><rect x="1" y="2" width="6" height="4.4" fill="none" stroke="#333" stroke-width=".6"/><path d="M1 2L4 4.5L7 2" fill="none" stroke="#333" stroke-width=".6"/></svg><b>PROMOTION</b><p>Short note on this next stage and the plan for the team and partners in the year.</p></div>
  <div class="edu-box" style="left:176px;top:36px"><svg width="8" height="8" viewBox="0 0 8 8"><path d="M1 1V7H7M2 6L4 3.5L5 5L7 2" fill="none" stroke="#333" stroke-width=".6"/></svg><b>GROWTH</b><p>Short note on this last stage and the plan for the team and partners in the year.</p></div>
  <p class="txt abs" style="left:28px;top:121px;width:215px;text-align:center">Our team builds new tools for cell research. We test each idea with care and share clear data with partners and investors at every stage of work, from early trials through to the clinic and beyond.</p>
  <div class="page-num">11</div>
</section>

<!-- 12 Donut bars -->
<section class="slide" style="left:600px;top:528px">
  <div class="brand"><i></i><span><b>Corvane</b><small>Therapeutics</small></span></div>
  <div class="abs" style="left:20px;top:13px">
    <div class="h-thin" style="font-size:10px;font-weight:500;color:var(--blue)">LOREM IPSUM</div>
    <div class="h-thin" style="font-size:10px;font-weight:500;color:var(--blue)">DOLOR SIT AMET</div>
  </div>
  <svg class="abs" style="left:0;top:48px" width="180" height="96" viewBox="0 0 180 96">
    <g>
      <rect x="70" y="3" width="93" height="10" fill="var(--blue)"/>
      <rect x="70" y="16" width="93" height="10" fill="#dcdcdc"/>
      <rect x="70" y="29" width="93" height="10" fill="var(--teal)"/>
      <rect x="70" y="42" width="93" height="10" fill="#dcdcdc"/>
      <rect x="70" y="55" width="93" height="10" fill="var(--blue)"/>
    </g>
    <g font-size="3.6" font-weight="700" fill="#fff" font-family="Poppins" text-anchor="end"><text x="150" y="9.5">Analysis</text><text x="150" y="22.5">Communication</text><text x="150" y="35.5">Recruitment</text><text x="150" y="48.5">Planning</text><text x="150" y="61.5">Management</text></g>
    <g fill="#fff"><circle cx="157" cy="8" r="2"/><circle cx="157" cy="21" r="2"/><circle cx="157" cy="34" r="2"/><circle cx="157" cy="47" r="2"/><circle cx="157" cy="60" r="2"/></g>
    <circle cx="56" cy="34" r="38" fill="#dcdcdc"/>
    <path d="M56 -4 A38 38 0 0 1 90 17 L56 34 Z" fill="var(--blue)"/>
    <path d="M90 17 A38 38 0 0 1 90 52 L56 34 Z" fill="#c9c9c9"/>
    <path d="M90 52 A38 38 0 0 1 40 69 L56 34 Z" fill="var(--teal)"/>
    <path d="M40 69 A38 38 0 0 1 19 46 L56 34 Z" fill="var(--blue)"/>
    <circle cx="56" cy="34" r="22" fill="#fff"/>
    <g font-size="5" font-weight="700" fill="#fff" font-family="Poppins"><text x="55" y="8">43%</text><text x="18" y="30">35%</text><text x="78" y="38">32%</text><text x="22" y="56">27%</text><text x="62" y="62">48%</text></g>
    <text x="44" y="32" font-size="3.8" font-weight="700" fill="#222">Your Text</text>
    <g fill="var(--blue)"><rect x="49" y="36" width="2" height="5"/><rect x="52" y="35" width="2" height="6"/><rect x="55" y="37" width="2" height="4"/><rect x="58" y="34" width="2" height="7"/></g>
  </svg>
  <div class="abs" style="left:188px;top:28px;width:72px">
    <div class="legend" style="position:relative;width:72px;margin-bottom:3px"><b style="padding:0;font-weight:700;font-size:3.4px">LOREM IPSUM</b><p style="padding:0">Short note on this key point for the plan and the team.</p></div>
    <div class="legend" style="position:relative;width:72px;margin-bottom:3px"><b style="padding:0;font-weight:700;font-size:3.4px">LOREM IPSUM</b><p style="padding:0">Short note on this key point for the plan and the team.</p></div>
    <div class="legend" style="position:relative;width:72px;margin-bottom:3px"><b style="padding:0;font-weight:700;font-size:3.4px">LOREM IPSUM</b><p style="padding:0">Short note on this key point for the plan and the team.</p></div>
    <div class="legend" style="position:relative;width:72px;margin-bottom:3px"><b style="padding:0;font-weight:700;font-size:3.4px">LOREM IPSUM</b><p style="padding:0">Short note on this key point for the plan and the team.</p></div>
    <div class="legend" style="position:relative;width:72px"><b style="padding:0;font-weight:700;font-size:3.4px">LOREM IPSUM</b><p style="padding:0">Short note on this key point for the plan and the team.</p></div>
  </div>
  <div class="footer-bar"></div><div class="page-num">12</div>
</section>

<!-- 13 Use cases -->
<section class="slide" style="left:39px;top:693px">
  <div class="brand"><i></i><span><b>Corvane</b><small>Therapeutics</small></span></div>
  <div class="photo" role="img" aria-label="Smartphone screen mockup" style="left:25px;top:20px;width:32px;height:66px;border:1.5px solid #222;border-radius:4px;background:linear-gradient(#ffffff,#eaf3fa)"></div>
  <div class="photo" role="img" aria-label="Smartphone screen mockup" style="left:64px;top:41px;width:32px;height:66px;border:1.5px solid #222;border-radius:4px;background:linear-gradient(#ffffff,#eaf3fa)"></div>
  <div class="photo" role="img" aria-label="Smartphone screen mockup" style="left:106px;top:63px;width:32px;height:66px;border:1.5px solid #222;border-radius:4px;background:linear-gradient(#ffffff,#eaf3fa)"></div>
  <div class="h-thin abs" style="left:149px;top:40px;font-size:16px;font-weight:500;color:var(--teal)">USE CASES</div>
  <p class="txt abs" style="left:149px;top:61px;width:110px">Our team builds new tools for cell research. We test each idea with care and share clear data with partners and investors at every stage of work, from early trials through to the clinic.</p>
  <p class="txt abs" style="left:149px;top:91px;width:110px">Our team builds new tools for cell research. We test each idea with care and share clear data with partners and investors at every stage of work, from early trials through to the clinic.</p>
  <div class="footer-bar"></div><div class="page-num">13</div>
</section>

<!-- 14 Company costs -->
<section class="slide" style="left:320px;top:693px">
  <div class="brand"><i></i><span><b>Corvane</b><small>Therapeutics</small></span></div>
  <div class="abs h-thin" style="left:0;width:271px;text-align:center;top:13px;font-size:12px;font-weight:500;color:var(--blue)">COMPANY COSTS</div>
  <p class="txt abs" style="left:16px;top:30px;width:239px;text-align:center">Our team builds new tools for cell research. We test each idea with care and share clear data with partners and investors at every stage of work, from early trials through to the clinic.</p>
  <p class="txt abs" style="left:20px;top:43px;width:231px;text-align:center">Each step below sets out where funds go and how we track costs over time with care.</p>
  <svg class="abs" style="left:0;top:56px" width="271" height="50" viewBox="0 0 271 50">
    <path d="M18 35H246" stroke="var(--blue)" stroke-width="3"/><path d="M245 31L251 35L245 39Z" fill="var(--blue)"/>
    <g font-size="3" font-weight="700" fill="#fff" font-family="Poppins"><text x="80" y="36">Step 01</text><text x="127" y="36">Step 02</text><text x="174" y="36">Step 03</text><text x="220" y="36">Step 04</text></g>
    <g fill="none" stroke-width="3"><path d="M44 30A14 14 0 1 1 72 30" stroke="var(--blue)"/><path d="M92 30A14 14 0 1 1 120 30" stroke="var(--teal)"/><path d="M139 30A14 14 0 1 1 167 30" stroke="var(--blue)"/><path d="M187 30A14 14 0 1 1 215 30" stroke="var(--blue)"/></g>
    <circle cx="58" cy="26" r="8" fill="var(--blue)"/><circle cx="106" cy="26" r="8" fill="var(--teal)"/><circle cx="153" cy="26" r="8" fill="var(--blue)"/><circle cx="201" cy="26" r="8" fill="var(--blue)"/>
    <g fill="none" stroke="#fff" stroke-width=".8"><circle cx="58" cy="26" r="4"/><path d="M58 23.5V26H60"/><circle cx="106" cy="26" r="3.5"/><ellipse cx="153" cy="24" rx="3.5" ry="1.3"/><path d="M149.5 24V28.5Q153 30 156.5 28.5V24"/><circle cx="200" cy="25" r="2.6"/><path d="M202 27L204 29"/></g>
    <g stroke="#999" stroke-width=".5"><path d="M62 40V50M110 40V50M157 40V50M205 40V50"/></g>
  </svg>
  <div class="mini-col" style="left:40px;top:111px;width:42px"><b>Lorem Ipsum</b>Short note on cost for this step and what it buys the team.</div>
  <div class="mini-col" style="left:89px;top:111px;width:42px"><b>Lorem Ipsum</b>Short note on cost for this step and what it buys the team.</div>
  <div class="mini-col" style="left:136px;top:111px;width:42px"><b>Lorem Ipsum</b>Short note on cost for this step and what it buys the team.</div>
  <div class="mini-col" style="left:184px;top:111px;width:42px"><b>Lorem Ipsum</b>Short note on cost for this step and what it buys the team.</div>
  <div class="footer-bar"></div><div class="page-num">14</div>
</section>

<!-- 15 Timeline infographic -->
<section class="slide" style="left:600px;top:693px">
  <div class="brand"><i></i><span><b>Corvane</b><small>Therapeutics</small></span></div>
  <div class="abs" style="left:49px;top:15px;display:flex;align-items:center;gap:3px;font-family:'Poppins',sans-serif;font-size:9px">
    <span style="color:var(--blue);letter-spacing:2.2px;font-weight:400">TIMELINE</span>
    <span style="background:var(--teal);color:#fff;font-weight:700;letter-spacing:1.6px;padding:0 3px">INFOGRAPHIC</span>
  </div>
  <svg class="abs" style="left:0;top:28px" width="271" height="115" viewBox="0 0 271 115">
    <path d="M45 58H233" stroke="#888" stroke-width=".5"/>
    <g fill="none" stroke="var(--blue)" stroke-width="1.6">
      <path d="M62 58V41A11 11 0 0 1 84 41V58"/>
      <path d="M131 58V41A11 11 0 0 1 153 41V58"/>
      <path d="M201 58V41A11 11 0 0 1 223 41V58"/>
    </g>
    <g fill="none" stroke="var(--teal)" stroke-width="1.6">
      <path d="M86 58V75A11 11 0 0 0 108 75V58"/>
      <path d="M155 58V75A11 11 0 0 0 177 75V58"/>
    </g>
    <g fill="var(--blue)"><circle cx="73" cy="33" r="3.2"/><circle cx="142" cy="33" r="3.2"/><circle cx="212" cy="33" r="3.2"/></g>
    <g fill="var(--teal)"><circle cx="97" cy="83" r="3.2"/><circle cx="166" cy="83" r="3.2"/></g>
    <g font-size="8" fill="#333" font-family="Roboto" text-anchor="middle"><text x="63" y="55">2018</text><text x="142" y="55">2020</text><text x="212" y="55">2022</text><text x="97" y="69">2029</text><text x="166" y="69">2021</text></g>
    <g fill="var(--teal)"><rect x="94" y="7" width="1.3" height="3"/><rect x="96" y="5" width="1.3" height="5"/><rect x="98" y="3" width="1.3" height="7"/></g>
    <path d="M164 4L169 1L168 6Z" fill="var(--teal)"/>
  </svg>
  <div class="mini-col" style="left:80px;top:43px;width:34px"><b style="font-size:2.8px;color:#222;font-weight:700">LOREM IPSUM</b>Short note on what the team did in this year of work.</div>
  <div class="mini-col" style="left:150px;top:43px;width:34px"><b style="font-size:2.8px;color:#222;font-weight:700">LOREM IPSUM</b>Short note on what the team did in this year of work.</div>
  <div class="mini-col" style="left:44px;top:95px;width:34px"><b style="font-size:2.8px;color:#222;font-weight:700">LOREM IPSUM</b>Short note on what the team did in this year of work.</div>
  <div class="mini-col" style="left:114px;top:95px;width:34px"><b style="font-size:2.8px;color:#222;font-weight:700">LOREM IPSUM</b>Short note on what the team did in this year of work.</div>
  <div class="mini-col" style="left:184px;top:95px;width:34px"><b style="font-size:2.8px;color:#222;font-weight:700">LOREM IPSUM</b>Short note on what the team did in this year of work.</div>
  <div class="footer-bar"></div><div class="page-num">15</div>
</section>

<!-- 16 Roadmap -->
<section class="slide" style="left:39px;top:856px">
  <div class="brand"><i></i><span><b>Corvane</b><small>Therapeutics</small></span></div>
  <svg class="abs" style="left:0;top:0" width="271" height="152" viewBox="0 0 271 152">
    <path d="M229 118V80" stroke="var(--blue)" stroke-width="1" stroke-dasharray="1.5 1.5"/>
    <path d="M229 80 C229 100 200 110 180 95 C160 82 140 92 128 82 C110 68 130 54 150 52 C170 50 190 40 180 32 C172 26 160 32 156 30" fill="none" stroke="var(--blue)" stroke-width="1.2"/>
    <path d="M180 95 C160 85 140 100 130 112 C120 122 110 118 100 110" fill="none" stroke="var(--blue)" stroke-width="1.2" stroke-dasharray="1.5 1.5"/>
    <path d="M156 30 C140 26 130 30 120 28 C110 26 104 24 96 20" fill="none" stroke="var(--blue)" stroke-width="1" stroke-dasharray="1.5 1.5"/>
    <g><circle cx="229" cy="65" r="17" fill="#fff" stroke="var(--teal)" stroke-width="2.5"/><text x="229" y="72" font-size="20" font-weight="700" fill="var(--blue)" text-anchor="middle" font-family="Poppins">1</text></g>
    <g><circle cx="145" cy="70" r="9" fill="#fff" stroke="var(--teal)" stroke-width="2"/><text x="145" y="74.5" font-size="11" font-weight="700" fill="var(--blue)" text-anchor="middle" font-family="Poppins">2</text></g>
    <g><circle cx="179" cy="50" r="7.5" fill="#fff" stroke="var(--teal)" stroke-width="1.8"/><text x="179" y="54" font-size="9" font-weight="700" fill="var(--blue)" text-anchor="middle" font-family="Poppins">3</text></g>
    <g><circle cx="119" cy="48" r="5" fill="#fff" stroke="var(--teal)" stroke-width="1.4"/><text x="119" y="50.5" font-size="6.5" font-weight="700" fill="var(--blue)" text-anchor="middle" font-family="Poppins">4</text></g>
    <g><circle cx="134" cy="40" r="4" fill="#fff" stroke="var(--teal)" stroke-width="1.2"/><text x="134" y="42" font-size="5" font-weight="700" fill="var(--blue)" text-anchor="middle" font-family="Poppins">5</text></g>
    <g><circle cx="102" cy="39" r="3" fill="#fff" stroke="var(--teal)" stroke-width="1"/><text x="102" y="40.6" font-size="4" font-weight="700" fill="var(--blue)" text-anchor="middle" font-family="Poppins">6</text></g>
  </svg>
  <div class="mini-col" style="left:53px;top:24px;width:30px;text-align:left"><b style="font-size:3px;color:#222;font-weight:700">LOREM IPSUM</b>Short note on this stage of the plan.</div>
  <div class="mini-col" style="left:146px;top:19px;width:32px;text-align:left"><b style="font-size:3px;color:#222;font-weight:700">LOREM IPSUM</b>Short note on this stage of the plan.</div>
  <div class="mini-col" style="left:190px;top:22px;width:32px;text-align:left"><b style="font-size:3px;color:#222;font-weight:700">LOREM IPSUM</b>Short note on this stage of the plan.</div>
  <div class="mini-col" style="left:97px;top:58px;width:32px;text-align:left"><b style="font-size:3px;color:#222;font-weight:700">LOREM IPSUM</b>Short note on this stage of the plan.</div>
  <div class="mini-col" style="left:182px;top:79px;width:32px;text-align:left"><b style="font-size:3px;color:#222;font-weight:700">LOREM IPSUM</b>Short note on this stage of the plan.</div>
  <div class="abs" style="left:20px;top:78px">
    <div class="h-thin" style="font-size:6.5px;letter-spacing:1.2px">TIMELINE OF</div>
    <div class="h-thin" style="font-size:11.5px;font-weight:600">ROADMAP</div>
    <div class="h-thin" style="font-size:5px;font-weight:600;color:var(--blue)">FOR 2 YEARS</div>
  </div>
  <div class="abs" style="left:20px;top:114px;display:flex;gap:5px;align-items:flex-start">
    <span style="width:13px;height:13px;border-radius:50%;background:var(--blue);color:#fff;font:700 7px 'Poppins',sans-serif;display:flex;align-items:center;justify-content:center">A</span>
    <div><b style="font:600 6px 'Poppins',sans-serif;color:#222">2019</b><p style="font-size:2.2px;line-height:1.3;color:var(--muted);width:28px">Short note on key aims set for this year.</p></div>
  </div>
  <div class="abs" style="left:78px;top:114px;display:flex;gap:5px;align-items:flex-start">
    <span style="width:13px;height:13px;border-radius:50%;background:var(--blue);color:#fff;font:700 7px 'Poppins',sans-serif;display:flex;align-items:center;justify-content:center">B</span>
    <div><b style="font:600 6px 'Poppins',sans-serif;color:#222">2020</b><p style="font-size:2.2px;line-height:1.3;color:var(--muted);width:28px">Short note on key aims set for this year.</p></div>
  </div>
  <div class="footer-bar"></div><div class="page-num">16</div>
</section>

<!-- 17 Text two column -->
<section class="slide" style="left:320px;top:856px">
  <div class="brand"><i></i><span><b>Corvane</b><small>Therapeutics</small></span></div>
  <div class="abs" style="left:12px;top:22px">
    <div class="h-thin" style="font-size:9.5px;color:var(--blue);font-weight:400">LOREM IPSUM</div>
    <div class="h-thin" style="font-size:9.5px;color:var(--blue);font-weight:600">DOLOR SIT AMET</div>
  </div>
  <div class="abs" style="left:12px;top:50px;width:123px;font-size:3.2px;line-height:1.25;color:#444">
    <p style="margin-bottom:4px">• <b style="color:var(--blue)">Lorem ipsum</b> : a short note on this point and its aims for the team.</p>
    <p style="margin-bottom:4px">• <b style="color:var(--blue)">Lorem ipsum</b> : a short note on this point and its aims for the team and partners with data.</p>
    <p style="margin-bottom:4px">• <b style="color:var(--blue)">Lorem ipsum</b> : a short note on this point and its aims for the team and partners with data.</p>
    <p style="margin-bottom:4px">• <b style="color:var(--blue)">Lorem ipsum</b> : a short note on this point and its aims for the team.</p>
    <p>• <b style="color:var(--blue)">Lorem ipsum</b> : a short note on this point and its aims for the team and partners with data.</p>
  </div>
  <div class="h-thin abs" style="left:150px;top:22px;font-size:7.8px;line-height:1.4;color:var(--teal)">WHAT'S A DOMAIN?<br>IT'S THAT NAME UP<br><b style="font-weight:700">IN THE ADDRESS BAR.</b></div>
  <ul class="squares abs" style="left:150px;top:63px;font-size:5px;list-style:none">
    <li style="margin-bottom:3.6px">Fits your business or products</li><li style="margin-bottom:3.6px">Is easy to spell and remember</li><li style="margin-bottom:3.6px">Fits your business or products</li><li style="margin-bottom:3.6px">Is easy to spell and remember</li><li style="margin-bottom:3.6px">Fits your business or products</li><li>Is easy to spell and remember</li>
  </ul>
  <div class="footer-bar"></div><div class="page-num">17</div>
</section>

<!-- 18 Options -->
<section class="slide" style="left:600px;top:856px">
  <div class="brand"><i></i><span><b>Corvane</b><small>Therapeutics</small></span></div>
  <div class="abs h-thin" style="left:17px;top:9px;font-size:9px;font-weight:500;color:var(--blue)">LOREM IPSUM <b style="font-weight:700">DOLOR SIT AMET</b></div>
  <svg class="abs" style="left:0;top:20px" width="271" height="105" viewBox="0 0 271 105">
    <g fill="none" stroke="var(--navy)" stroke-width="1.8">
      <circle cx="110" cy="34" r="11"/><circle cx="152" cy="34" r="11"/><circle cx="85" cy="65" r="11"/><circle cx="177" cy="65" r="11"/>
      <path d="M110 45 Q118 60 131 64M152 45 Q144 60 131 64M96 65 H115M166 65 H147"/>
    </g>
    <circle cx="131" cy="78" r="18" fill="var(--teal)"/>
    <circle cx="131" cy="78" r="15" fill="none" stroke="var(--blue)" stroke-width="4" stroke-dasharray="3 1.5"/>
    <circle cx="131" cy="78" r="10" fill="#fff"/>
    <g font-size="3.2" font-weight="600" fill="#222" text-anchor="middle" font-family="Poppins"><text x="110" y="39">Option B</text><text x="152" y="39">Option C</text><text x="85" y="70">Option A</text><text x="177" y="70">Option D</text></g>
    <g fill="var(--blue)"><rect x="107" y="28" width="6" height="4"/><path d="M147 30L152 28L157 30L152 32Z"/><rect x="82" y="59" width="6" height="4"/><rect x="174" y="59" width="6" height="4"/></g>
  </svg>
  <div class="mini-col" style="left:64px;top:33px;width:30px"><b style="font-size:3.4px">Your Title</b>Short note on this option and what it offers.</div>
  <div class="mini-col" style="left:168px;top:32px;width:32px;text-align:left"><b style="font-size:3.4px">Your Title</b>Short note on this option and what it offers.</div>
  <div class="mini-col" style="left:38px;top:64px;width:30px"><b style="font-size:3.4px">Your Title</b>Short note on this option and what it offers.</div>
  <div class="mini-col" style="left:194px;top:66px;width:32px;text-align:left"><b style="font-size:3.4px">Your Title</b>Short note on this option and what it offers.</div>
  <p class="txt abs" style="left:30px;top:123px;width:211px;text-align:center">Our team builds new tools for cell research. We test each idea with care and share clear data with partners and investors at every stage of work, from early trials through to the clinic.</p>
  <div class="page-num">18</div>
</section>

<!-- 19 Domain lists -->
<section class="slide" style="left:39px;top:1021px">
  <div class="brand"><i></i><span><b>Corvane</b><small>Therapeutics</small></span></div>
  <div class="h-thin abs" style="left:21px;top:18px;font-size:9px;color:var(--teal)">WHAT'S A DOMAIN? IT'S THAT NAME UP</div>
  <div class="h-bold abs" style="left:21px;top:31px;font-size:12px;font-weight:700">IN THE ADDRESS BAR.</div>
  <ul class="squares abs" style="left:21px;top:56px">
    <li>Fits your business or products</li><li>Is easy to spell and remember</li><li>Fits your business or products</li><li>Is easy to spell and remember</li><li>Fits your business or products</li><li>Is easy to spell and remember</li>
  </ul>
  <ul class="squares abs" style="left:144px;top:56px">
    <li>Fits your business or products</li><li>Is easy to spell and remember</li><li>Fits your business or products</li><li>Is easy to spell and remember</li><li>Fits your business or products</li><li>Is easy to spell and remember</li>
  </ul>
  <div class="footer-bar"></div><div class="page-num">19</div>
</section>

<!-- 20 Team -->
<section class="slide" style="left:320px;top:1021px">
  <div class="brand"><i></i><span><b>Corvane</b><small>Therapeutics</small></span></div>
  <div class="abs h-bold" style="left:0;width:271px;text-align:center;top:20px;font-size:8.5px;font-weight:600;color:var(--teal)">TEAM MEMBERS AND ADVISORS</div>
  <p class="txt abs" style="left:15px;top:33px;width:241px;text-align:center">Our team builds new tools for cell research. We test each idea with care and share clear data with partners and investors at every stage of work, from early trials through to the clinic and beyond.</p>
  <p class="txt abs" style="left:15px;top:47px;width:241px;text-align:center">Each person below brings deep skill in science, business and care for patients.</p>
  <div class="abs" style="left:0;top:61px;width:271px;height:73px;background:var(--blue)"></div>
  <div class="person" style="left:19px"><div class="avatar" role="img" aria-label="Team member portrait"></div><b>JONAH REYES</b><p>Short bio on role, past work and the skills this person brings.</p></div>
  <div class="person" style="left:83px"><div class="avatar" role="img" aria-label="Team member portrait"></div><b>MARA ELLISON</b><p>Short bio on role, past work and the skills this person brings.</p></div>
  <div class="person" style="left:147px"><div class="avatar" role="img" aria-label="Advisor portrait"></div><b>JONAH REYES</b><p>Short bio on role, past work and the skills this person brings.</p></div>
  <div class="person" style="left:212px"><div class="avatar" role="img" aria-label="Advisor portrait"></div><b>MARA ELLISON</b><p>Short bio on role, past work and the skills this person brings.</p></div>
  <div class="page-num">20</div>
</section>

<!-- 21 Thank you -->
<section class="slide" style="left:600px;top:1021px">
  <div class="abs" style="left:20px;top:60px;display:flex;align-items:center;gap:3px;color:var(--blue);font-family:'Poppins',sans-serif;font-weight:600">
    <i style="display:block;width:11px;height:11px;border:2px solid var(--blue);border-radius:50%"></i>
    <span style="display:flex;flex-direction:column;line-height:.85"><b style="font-size:16px;font-weight:600">Corvane</b><small style="font-size:5.5px;font-weight:600;margin-left:8px">Therapeutics</small></span>
  </div>
  <div class="abs h-bold" style="left:117px;top:54px;font-size:12px;font-weight:600;color:#222">THANK YOU</div>
  <div class="abs h-bold" style="left:117px;top:70px;font-size:7px;font-weight:700">CONTACT US</div>
  <div class="abs" style="left:117px;top:81px;font-size:4px;line-height:1.6;color:#333">
    <div><span style="color:var(--teal)">●</span> 555-014-2290</div>
    <div><span style="color:var(--teal)">●</span> hello@corvanebio.com</div>
    <div><span style="color:var(--teal)">●</span> Your address, your city, box 88900</div>
  </div>
  <div class="abs" style="left:0;bottom:0;width:271px;height:4px;background:var(--blue)"></div>
</section>

</div>
</body>
</html>
```